Elegant and modern body scrub for organic junkies

I need a package design for my new company based out of Austin, Texas. We are focused on cruelty free and all natural and organic products. Our deign needs to be able to have the information we require on it, while still appearing very clean and captivating. Our initial product is a clear skin body scrub, intended for people with problematic skin. Our target market is women and we want to show elegance, without appearing "high end."
Updates

Reason: I want to allot more time for certain designers to submit edits. Last minute proposals have been appealing

Target Market(s)

Women. Organic and holistic minded. Natural beauty lovers.

Industry/Entity Type

Skin Care Product

Font styles to use
Script
Other font styles liked:
• AmericanTypewriter, Beautifulflaws, courier, caviarDreams-bold

Colors
000000
ffc214
ffffff
fece3e
fbee3e

Requirements
Must have
• Must be designed in Adobe Illustrator.
• The photo titled “structure for oz and grams” -That needs to be included at the bottom of 1B. I like the horizontal and vertical bar that separate the two. I want that.
• Color Inspiration - The photo titled “vorna color inspiration” and “color combo inspiration” are the colors I want. BLACK, GOLD, WHITE. I want the label background black and the writing in white with some gold somewhere on it. My logo is going to be a golden elephant.
• The photos titled “I like how clean this looks” and “I also like how clean this looks” - I want 1B to look super clean. I don’t want a lot of information in this box. I want simple and clean. This is where the logo and brand name will go.
• Logo - A golden elephant. I want it to be gold and geometric. There can be dimension like this elephant example on the left of the 1B description. I want the trunk to be facing to the left and the trunk needs to be raised overhead and touching the animal's forehead.
• The photo titled “sideways writing and silver rim” - I want 1C to be written sideways like this. My text will be much more extensive so the font won’t be able to be so big.
Nice to have
• The photo titled “sideways writing and silver rim” - I want 1C to be written sideways like this. My text will be much more extensive so the font won’t be able to be so big. I also REALLY like how this label is rimmed in silver, but I would want gold. This is not mandatory, but I really like this.
• The photo titled “melted honey” - This is another option I really like. The gold that looks like honey dripping on the label is really cool. Not mandatory, but I really liked that. I also like the craft background on this.
• Color Inspiration - The photo titled “color inspiration” and “another color inspiration” is an option I would also like to see. Rather than black, I’d like to see what it would ALSO look like with a navy background. NAVY, GOLD, WHITE, maybe black somewhere.
Should not have
• Colorful patterns or excessive info in section 1B.

```html
<!DOCTYPE html>
<html lang="en">
<head>
<meta charset="utf-8">
<title>Body Scrub Label</title>
<link rel="stylesheet" href="https://fonts.googleapis.com/css2?family=Josefin+Sans:ital,wght@0,300;0,700;1,300&display=swap">
<style>
  :root {
    --page: #ffffff;
    --ink: #000000;
    --panel: #fcfcfb;
    --gold: #d9a514;
    --gold-light: #fece3e;
    --gold-deep: #b8860b;
    --rule: #d8d2c4;
  }
  * { margin: 0; padding: 0; box-sizing: border-box; }
  html, body {
    width: 1200px;
    height: 645px;
    overflow: hidden;
    background: var(--page);
  }
  .canvas {
    position: relative;
    width: 1200px;
    height: 645px;
  }
  .label {
    position: absolute;
    left: 228px;
    top: 143px;
    width: 747px;
    height: 357px;
  }
  .label__marble {
    position: absolute;
    inset: 0;
    background:
      radial-gradient(ellipse at 2% 55%, rgba(217,165,20,0.35), transparent 18%),
      radial-gradient(ellipse at 98% 65%, rgba(217,165,20,0.35), transparent 16%),
      radial-gradient(ellipse at 45% 2%, rgba(217,165,20,0.25), transparent 22%),
      var(--ink);
  }
  .label__panel {
    position: absolute;
    left: 16px;
    top: 15px;
    width: 717px;
    height: 330px;
    background: var(--panel);
  }
  .label__frame {
    position: absolute;
    inset: 8px;
    border: 2px solid var(--gold);
  }
  .label__frame::after {
    content: "";
    position: absolute;
    inset: 3px;
    border: 1px solid var(--gold-light);
  }
  .brand-mark {
    position: absolute;
    left: 50%;
    top: 80px;
    width: 76px;
    height: 76px;
    margin-left: -38px;
    border-radius: 50%;
    background: linear-gradient(135deg, var(--gold-light), var(--gold) 55%, var(--gold-deep));
  }
  .brand-name {
    position: absolute;
    left: 0;
    right: 0;
    top: 187px;
    text-align: center;
    font-family: "Josefin Sans", sans-serif;
    font-weight: 700;
    font-size: 36px;
    letter-spacing: 0.17em;
    color: var(--ink);
    padding-left: 0.17em;
  }
  .net-weight {
    position: absolute;
    left: 115px;
    top: 281px;
    width: 480px;
    height: 26px;
    border-top: 1px solid var(--rule);
    font-family: "Josefin Sans", sans-serif;
    font-style: italic;
    font-weight: 300;
    font-size: 12px;
    color: var(--gold);
  }
  .net-weight__divider {
    position: absolute;
    left: 241px;
    top: 0;
    width: 1px;
    height: 25px;
    background: var(--rule);
  }
  .net-weight__imperial,
  .net-weight__metric {
    position: absolute;
    top: 9px;
  }
  .net-weight__imperial { left: 159px; }
  .net-weight__metric { left: 302px; }
</style>
</head>
<body>
  <main class="canvas">
    <section class="label">
      <div class="label__marble" role="img" aria-label="Black marble background with gold veins"></div>
      <div class="label__panel">
        <div class="label__frame"></div>
        <div class="brand-mark" aria-hidden="true"></div>
        <h1 class="brand-name">BRAND NAME</h1>
        <div class="net-weight">
          <span class="net-weight__imperial">12OZ</span>
          <span class="net-weight__divider"></span>
          <span class="net-weight__metric">340 g</span>
        </div>
      </div>
    </section>
  </main>
</body>
</html>
```